Design einer Angebotsmappe
Zielgruppe
Wir sind ein Handwerksbetrieb im Bereich Elektrotechnik.
Wir betreuen private Haushalte, Gewerbekunden oder Architekten.
Mehr über uns : www.kessler-brandau.de
Aufgabenstellung
Es soll das Design für eine Angebotsmappe erstellt werden. Die Mappe soll einen sehr hochwertigen und professionellen Eindruck beim Kunden machen.
Unser Logo soll auf der Vorderseite platziert werden und mit partiellen UV Lack in Szene gesetzt werden.
Alles andere ist Ihrer Kreativität überlassen.
-An geeigneter Stelle soll auf unsere Profile bei Instagram & Facebook hingewiesen werden mit passenden Icon und Accountname.
-Sowie ein Hinweis auf unsere Internetseite www.kessler-brandau.de
Zu beachten sind die Druckvorgaben im Anhang

```html
<!DOCTYPE html>
<html lang="de">
<head>
<meta charset="utf-8">
<title>Angebotsmappe Kessler &amp; Brandau Elektrotechnik</title>
<link rel="stylesheet" href="https://fonts.googleapis.com/css2?family=Roboto:wght@400;500;700&family=Roboto+Condensed:wght@400;700&display=swap">
<style>
  :root{
    --bg:#d4d4d4;
    --blue:#1f97da;
    --blue-light:#27a3e6;
    --blue-dark:#2379ad;
    --paper:#ffffff;
    --panel:#efefef;
    --sheet:#f6f6f6;
    --ink:#1c1c1c;
    --ink-soft:#555;
  }
  *{box-sizing:border-box;margin:0;padding:0}
  html,body{width:1200px;height:1200px;overflow:hidden}
  body{
    background:radial-gradient(circle at 50% 45%,#f4f4f4 0%,var(--bg) 75%);
    font-family:"Roboto",Arial,sans-serif;
    position:relative;
  }
  .spread{position:absolute;left:90px;width:1020px;height:476px;display:flex;box-shadow:0 10px 30px rgba(0,0,0,.18)}
  .spread--inside{top:60px}
  .spread--outside{top:640px}
  .panel{position:relative;width:340px;height:100%;overflow:hidden}

  /* inside */
  .inside-left{background:linear-gradient(100deg,#fafafa,#e9e9e9)}
  .inside-center{background:var(--panel)}
  .inside-right{background:var(--paper)}

  .letter{position:absolute;left:18px;top:8px;width:304px;height:440px;background:var(--sheet);box-shadow:0 1px 4px rgba(0,0,0,.15);padding:34px 36px;font-size:5.6px;color:var(--ink-soft);line-height:1.45}
  .brand{display:flex;align-items:center;gap:5px;font-weight:700;color:var(--blue);letter-spacing:.04em;text-transform:uppercase}
  .brand__dot{width:12px;height:12px;border-radius:50%;background:var(--blue)}
  .letter .brand{position:absolute;right:36px;top:30px;font-size:7.5px}
  .letter__recipient{margin-top:44px;color:var(--ink);font-weight:500}
  .letter__date{text-align:right;margin-top:10px}
  .letter__subject{font-size:7.5px;color:var(--ink);font-weight:500;margin-top:14px}
  .letter p{margin-top:10px}
  .letter__signatures{width:110px;height:28px;margin-top:12px;background:linear-gradient(90deg,#dbe8f3,#e9f0f6)}
  .letter__signer{margin-top:10px}

  .pocket{position:absolute;left:0;bottom:0;width:340px;height:88px;background:var(--blue);clip-path:polygon(0 16%,8% 0,92% 0,100% 16%,100% 100%,0 100%)}
  .card{position:absolute;left:30px;bottom:6px;width:124px;height:76px;background:#f1f1f1;box-shadow:0 1px 4px rgba(0,0,0,.25);display:flex;align-items:center;justify-content:center}
  .card .brand{font-size:7px}
  .socials{list-style:none;color:#fff;font-weight:500}
  .socials li{display:flex;align-items:center;gap:6px}
  .socials__mark{width:9px;height:9px;border-radius:50%;border:1.5px solid #fff}
  .pocket .socials{position:absolute;left:172px;top:24px;font-size:6.8px}
  .pocket .socials li+li{margin-top:6px}

  .team{position:absolute;left:18px;top:14px;width:304px;height:446px;background:linear-gradient(180deg,#63acdd 0%,#3e93cf 55%,#2b86c8 100%)}
  .team__photo{position:absolute;inset:0 0 118px 0;background:linear-gradient(180deg,#7bb9e4,#4d9bd3)}
  .team__text{position:absolute;left:14px;right:14px;bottom:14px;color:#fff;font-size:6px;line-height:1.45}
  .team__text p+p{margin-top:6px}
  .team__sign{display:flex;justify-content:space-between;align-items:center;margin-top:8px}
  .team__sign span:last-child{width:96px;height:22px;background:rgba(255,255,255,.25)}

  /* outside */
  .outside-back{background:linear-gradient(160deg,var(--blue-light),var(--blue))}
  .outside-center{background:linear-gradient(180deg,var(--blue-light),var(--blue))}
  .outside-front{background:var(--blue-dark)}
  .welcome{position:absolute;left:0;right:60px;top:196px;text-align:center;color:#fff;font-family:"Roboto Condensed",Arial,sans-serif;font-size:11px;line-height:1.35}
  .welcome small{display:block;margin-top:6px;font-size:8px;opacity:.85}
  .website{position:absolute;left:0;right:0;top:188px;text-align:center;color:#fff;font-weight:700;font-size:17px}
  .outside-center .socials{position:absolute;left:82px;top:224px;font-size:9px}
  .outside-center .socials li+li{margin-top:8px}
  .outside-center .socials__mark{width:11px;height:11px}
  .contact{position:absolute;left:0;right:0;bottom:26px;display:flex;justify-content:center;gap:14px;color:#fff;font-size:6.2px;list-style:none}
  .contact li{display:flex;align-items:center;gap:4px}
  .contact svg{width:8px;height:8px;fill:#fff}
  .outside-front .brand{position:absolute;left:0;right:0;top:210px;justify-content:center;color:#fff;font-size:12px}
  .outside-front .brand__dot{width:16px;height:16px;background:none;border:2px solid #fff}
</style>
</head>
<body>

<section class="spread spread--inside" aria-label="Innenseite der Mappe">
  <div class="panel inside-left"></div>

  <div class="panel inside-center">
    <article class="letter">
      <div class="brand"><span class="brand__dot"></span>Kessler &amp; Brandau</div>
      <div class="letter__recipient">Musterfirma<br>Musterabteilung<br>Muster Str. 57<br>76543 Musterdorf</div>
      <div class="letter__date">Lindenallee 14, 21465 Wentorf, 20. April 2020</div>
      <div class="letter__subject">Moin moin</div>
      <p>Sehr geehrter Herr Muster,</p>
      <p>Lorem ipsum dolor sit amet, consectetuer adipiscing elit, sed diam nonummy nibh euismod tincidunt ut laoreet dolore magna aliquam erat volutpat. Ut wisi enim ad minim veniam, quis nostrud exerci tation ullamcorper suscipit lobortis nisl ut aliquip ex ea commodo consequat. Duis autem vel eum iriure dolor in hendrerit in vulputate velit esse molestie consequat, vel illum dolore eu feugiat nulla facilisis at vero eros et accumsan et iusto odio dignissim qui blandit praesent luptatum zzril delenit augue duis dolore te feugait nulla facilisi.</p>
      <p>Mit freundlichen Grüßen</p>
      <div class="letter__signatures" role="img" aria-label="Handschriftliche Unterschriften der Geschäftsführer"></div>
      <div class="letter__signer">Jonas Kessler und Felix Wandrup</div>
    </article>
    <div class="pocket">
      <div class="card"><div class="brand"><span class="brand__dot"></span>Kessler &amp; Brandau</div></div>
      <ul class="socials">
        <li><span class="socials__mark"></span>kessler_brandau_elektrotechnik</li>
        <li><span class="socials__mark"></span>kesslerbrandauelektrotechnik</li>
      </ul>
    </div>
  </div>

  <div class="panel inside-right">
    <div class="team">
      <div class="team__photo" role="img" aria-label="Foto der beiden Geschäftsführer vor Firmentransportern, blau eingefärbt"></div>
      <div class="team__text">
        <p>Die Firma Kessler &amp; Brandau Elektrotechnik GmbH &amp; Co. KG ist Ihr zuverlässiger Partner für alle Fragen in der Elektrotechnik.</p>
        <p>Unser junges aufstrebendes Unternehmen wurde von Jonas Kessler und Felix Wandrup in Wentorf gegründet. Wir stehen für einen freundlichen und fairen Umgang mit unseren Kunden und für eine reibungslose Auftragsabwicklung sowie für die fachlich kompetente Beratung vor, während und nach der Bauphase.</p>
        <div class="team__sign"><span>Ihr Elektriker in Wentorf und Umland!</span><span role="img" aria-label="Unterschriften"></span></div>
      </div>
    </div>
  </div>
</section>

<section class="spread spread--outside" aria-label="Außenseite der Mappe">
  <div class="panel outside-back">
    <div class="welcome">Willkommen<br>bei Ihrem Elektriker in Wentorf<small>Kessler &amp; Brandau Elektrotechnik</small></div>
  </div>

  <div class="panel outside-center">
    <div class="website">www.kessler-brandau.de</div>
    <ul class="socials">
      <li><span class="socials__mark"></span>kessler_brandau_elektrotechnik</li>
      <li><span class="socials__mark"></span>kesslerbrandauelektrotechnik</li>
    </ul>
    <ul class="contact">
      <li><svg viewBox="0 0 10 10"><path d="M5 0a3.5 3.5 0 0 0-3.5 3.5C1.5 6 5 10 5 10s3.5-4 3.5-6.5A3.5 3.5 0 0 0 5 0zm0 5a1.5 1.5 0 1 1 0-3 1.5 1.5 0 0 1 0 3z"/></svg>Lindenallee 14, 21465 Wentorf</li>
      <li><svg viewBox="0 0 10 10"><path d="M2 0l2 2.5-1.2 1.2a6 6 0 0 0 3.5 3.5L7.5 6 10 8 8.5 10C4 10 0 6 0 1.5z"/></svg>040 - 73918204</li>
      <li><svg viewBox="0 0 10 10"><path d="M0 2h10v6H0zM0 2l5 3.5L10 2" stroke="#1f97da" stroke-width=".8"/></svg>info@kessler-brandau.de</li>
    </ul>
  </div>

  <div class="panel outside-front">
    <div class="brand"><span class="brand__dot"></span>Kessler &amp; Brandau</div>
  </div>
</section>

</body>
</html>
```